Simple Business Cards for Self-employed Coach

Simple business card with a design that includes the QLT logo.
Using either only the logo color or additional colors that match the logo.

Meridian Guides reach deeply into the past, gathering wisdom from East and West, while still staying current with the frontiers of new discovery in cognitive science, genetics, and other disciplines. see https://www.brightharborpath.example/what-is-integral-coaching/

Target Market(s)

Coaching Clients in Tokyo /Asia; in business organizations, but also outside

Industry/Entity Type

Life Coaching

Contact Information for Business Card

Lukas Brenning
Certified Meridian Guide

3-2-48 Kamiyoshi
Nakarino 164-0392
Tokyo, Japan

Phone: +81 70 4817 5062
E-Mail: lukas.brenning@mailora.example

Font styles to use
Sans Serif

Colors
00a990

Requirements
Must have
• include uploaded logo
• color fitting with QLT logo color
Nice to have
• simple, elegant design
Should not have
• clutter

```html
<!DOCTYPE html>
<html lang="en">
<head>
<meta charset="utf-8">
<title>QLT Business Card – Lukas Brenning</title>
<link rel="stylesheet" href="https://fonts.googleapis.com/css2?family=Source+Sans+3:wght@400;600;700&display=swap">
<style>
  :root {
    --brand: #00a990;
    --card: #ffffff;
    --backdrop: #f4f4f4;
    --edge: #e2e2e2;
  }
  * { margin: 0; padding: 0; box-sizing: border-box; }
  html, body {
    width: 1200px;
    height: 1011px;
    overflow: hidden;
    background: var(--backdrop);
    font-family: "Source Sans 3", sans-serif;
    color: var(--brand);
  }
  .stage {
    width: 1200px;
    height: 1011px;
    display: flex;
    align-items: center;
    justify-content: center;
  }
  .business-card {
    position: relative;
    width: 840px;
    height: 480px;
    background: var(--card);
    border: 1px solid var(--edge);
    box-shadow: 0 10px 30px rgba(0,0,0,0.06);
  }
  .brand-mark {
    position: absolute;
    left: 90px;
    top: 120px;
    display: flex;
    align-items: center;
    gap: 16px;
  }
  .brand-square {
    width: 34px;
    height: 34px;
    background: var(--brand);
  }
  .brand-name {
    font-size: 58px;
    font-weight: 700;
    letter-spacing: 10px;
    line-height: 1;
  }
  .contact-block {
    position: absolute;
    left: 440px;
    top: 120px;
  }
  .person-name {
    font-size: 38px;
    font-weight: 700;
    line-height: 1;
    letter-spacing: -0.5px;
    text-transform: uppercase;
  }
  .person-title {
    margin-top: 8px;
    font-size: 19px;
    font-weight: 400;
    text-transform: uppercase;
    letter-spacing: 0.2px;
  }
  .address {
    margin-top: 26px;
    width: 270px;
    text-align: center;
    font-size: 19px;
    line-height: 1.35;
    font-style: normal;
  }
  .contact-lines {
    margin-top: 18px;
    margin-left: -30px;
    font-size: 19px;
    line-height: 1.35;
  }
  .contact-label { font-weight: 700; }
</style>
</head>
<body>
  <main class="stage">
    <section class="business-card">
      <div class="brand-mark">
        <span class="brand-square"></span>
        <span class="brand-name">QLT</span>
      </div>
      <div class="contact-block">
        <h1 class="person-name">Lukas Brenning</h1>
        <p class="person-title">Certified Meridian Guide</p>
        <address class="address">
          3-2-48 Kamiyoshi<br>
          Nakarino 164-0392<br>
          Tokyo, Japan
        </address>
        <p class="contact-lines">
          <span class="contact-label">T:</span> +81 70 4817 5062<br>
          <span class="contact-label">E:</span> lukas.brenning@mailora.example
        </p>
      </div>
    </section>
  </main>
</body>
</html>
```